New Business Card Design Project

Looking for a modern business card design for an import distribution business for industrial technical products. The winning design will translate modern, sophistication, technical, professional and sustainable.

Target Market(s)

Technical customers

Industry/Entity Type

Business

Contact Information for Business Card

Dean Harlow
Sales Manager
M: 0471 625 183
P: 1300 872 619
dean@volkarsystems.com.au
4/18 Galloway Crest Road
Kellmore Vale NSW 2163
www.volkarsystems.com.au

Font styles to use
Sans Serif

Colors
ec1f27
606060
000000
fbfbfb

Requirements
Must have
• My Logo which is the Volkar Systems logo attached
Nice to have
• Eurostile Bold font

```html
<!DOCTYPE html>
<html lang="en">
<head>
<meta charset="utf-8">
<title>Volkar Systems – Business Card</title>
<link href="https://fonts.googleapis.com/css2?family=PT+Sans:wght@400;700&display=swap" rel="stylesheet">
<style>
  :root {
    --brand-red: #ec1f27;
    --brand-grey: #606060;
    --ink: #2e2e2e;
    --paper: #fbfbfb;
    --stage: #e6e6e6;
    --strip-a: #d9d2cd;
    --strip-b: #c9c9c9;
  }
  * { box-sizing: border-box; margin: 0; padding: 0; }
  html, body {
    width: 1200px;
    height: 1200px;
    overflow: hidden;
    background: var(--stage);
    font-family: "PT Sans", sans-serif;
  }
  .sheet {
    width: 1200px;
    height: 1200px;
    display: flex;
    flex-direction: column;
    align-items: center;
    justify-content: center;
    gap: 52px;
  }
  .card {
    position: relative;
    width: 900px;
    height: 514px;
    background: var(--paper);
    box-shadow: 0 2px 10px rgba(0,0,0,0.12);
    overflow: hidden;
  }
  .card__edge-pattern {
    position: absolute;
    left: 0; top: 0; bottom: 0;
    width: 34px;
    background: linear-gradient(90deg, var(--strip-a), var(--strip-b));
    opacity: 0.75;
  }

  /* Back side */
  .card--back {
    display: flex;
    align-items: center;
    justify-content: center;
  }
  .wordmark {
    display: flex;
    align-items: center;
    gap: 18px;
  }
  .wordmark__square {
    width: 56px;
    height: 56px;
    background: var(--brand-red);
  }
  .wordmark__name {
    color: var(--brand-red);
    font-weight: 700;
    font-size: 58px;
    letter-spacing: 1px;
    line-height: 1;
  }

  /* Front side */
  .card--front {
    display: flex;
    align-items: center;
  }
  .front__brand {
    width: 370px;
    padding-left: 40px;
    display: flex;
    flex-direction: column;
    align-items: center;
    gap: 18px;
  }
  .front__brand .wordmark__square { width: 110px; height: 110px; }
  .front__brand .wordmark__name { font-size: 40px; }
  .front__divider {
    width: 2px;
    height: 220px;
    background: var(--brand-grey);
    opacity: 0.8;
  }
  .front__details {
    padding-left: 46px;
    display: flex;
    flex-direction: column;
  }
  .person {
    display: flex;
    align-items: flex-start;
    gap: 14px;
    margin-bottom: 34px;
  }
  .person__arrow { width: 32px; height: 32px; margin-top: 6px; }
  .person__name {
    color: var(--brand-red);
    font-weight: 700;
    font-size: 50px;
    line-height: 1;
  }
  .person__title {
    color: var(--brand-grey);
    font-size: 21px;
    margin-top: 4px;
  }
  .contact-list { list-style: none; }
  .contact-list__item {
    display: flex;
    align-items: flex-start;
    gap: 16px;
    color: var(--ink);
    font-size: 24px;
    line-height: 31px;
  }
  .contact-list__icon {
    width: 24px;
    height: 24px;
    margin-top: 3px;
    flex: none;
  }
</style>
</head>
<body>
<main class="sheet">

  <section class="card card--back" aria-label="Card back">
    <div class="card__edge-pattern" role="img" aria-label="Decorative zigzag edge pattern in soft grey and peach"></div>
    <div class="wordmark">
      <span class="wordmark__square"></span>
      <span class="wordmark__name">Volkar Systems</span>
    </div>
  </section>

  <section class="card card--front" aria-label="Card front">
    <div class="card__edge-pattern" role="img" aria-label="Decorative zigzag edge pattern in soft grey and peach"></div>

    <div class="front__brand">
      <span class="wordmark__square"></span>
      <span class="wordmark__name">Volkar Systems</span>
    </div>

    <div class="front__divider"></div>

    <div class="front__details">
      <div class="person">
        <svg class="person__arrow" viewBox="0 0 32 32" aria-hidden="true">
          <path d="M6 26 L24 8 M11 8 H24 V21" fill="none" stroke="#a8a8a8" stroke-width="5" stroke-linecap="square"/>
        </svg>
        <div>
          <div class="person__name">Dean Harlow</div>
          <div class="person__title">Sales Manager</div>
        </div>
      </div>

      <ul class="contact-list">
        <li class="contact-list__item">
          <svg class="contact-list__icon" viewBox="0 0 24 24" aria-hidden="true">
            <circle cx="12" cy="12" r="12" fill="var(--brand-red)"/>
            <path d="M6 10 Q12 5 18 10 L16 12 L14 10 H10 L8 12 Z M8 13 H16 V17 H8 Z" fill="#fff"/>
          </svg>
          <span>0471 625 183<br>1300 872 619</span>
        </li>
        <li class="contact-list__item">
          <svg class="contact-list__icon" viewBox="0 0 24 24" aria-hidden="true">
            <circle cx="12" cy="12" r="12" fill="var(--brand-red)"/>
            <rect x="6" y="8" width="12" height="8" fill="#fff"/>
            <path d="M6 8 L12 13 L18 8" fill="none" stroke="var(--brand-red)" stroke-width="1.5"/>
          </svg>
          <span>dean@volkarsystems.com.au</span>
        </li>
        <li class="contact-list__item">
          <svg class="contact-list__icon" viewBox="0 0 24 24" aria-hidden="true">
            <circle cx="12" cy="12" r="12" fill="var(--brand-red)"/>
            <circle cx="12" cy="12" r="6" fill="none" stroke="#fff" stroke-width="1.6"/>
            <path d="M6 12 H18 M12 6 Q8.5 12 12 18 M12 6 Q15.5 12 12 18" fill="none" stroke="#fff" stroke-width="1.3"/>
          </svg>
          <span>www.volkarsystems.com.au</span>
        </li>
        <li class="contact-list__item">
          <svg class="contact-list__icon" viewBox="0 0 24 24" aria-hidden="true">
            <circle cx="12" cy="12" r="12" fill="var(--brand-red)"/>
            <path d="M12 19 C8 14 8 12 8 10.5 A4 4 0 0 1 16 10.5 C16 12 16 14 12 19 Z" fill="#fff"/>
            <circle cx="12" cy="10.5" r="1.6" fill="var(--brand-red)"/>
          </svg>
          <span>4/18 Galloway Crest Road<br>Kellmore Vale NSW 2163</span>
        </li>
      </ul>
    </div>
  </section>

</main>
</body>
</html>
```